Wix web design for healthcare IT consulting firm.

I am looking for a web design built in Wix that it will be easy for me to add or edit content in the future. The web site does not need to be overly complicated, but it should look very polished and professional. I also want to ensure it is mobile device friendly. I do not need any type of on-line purchasing ability. I will eventually do blogs, but for now it is a fairly standard web site with main page, about us, services provided, etc. I would also like a place for potential customers to contact us directly from the web site. I have included a Word document with some content for the web design. I have also included my logo and business card for reference. I would like to utilize similar colors as my business card. One of my primary competitors is https://vonmarlhq.example/

Target Market(s)

Target market could be nursing home CEO, CIO, or other leader at an organization that manages long term care facilities.

Number of Pages Required

5+ page

Colors
876aae

Requirements
Must have
• Be designed to be used in Wix. Use the content I provided to create and make web design. Allow to be viewed on mobile device. Please use similar color structure as attached business card. Please use attached logo in design.

```html
<!DOCTYPE html>
<html lang="en">
<head>
<meta charset="utf-8">
<title>ClearPath Health Solutions</title>
<link href="https://fonts.googleapis.com/css2?family=Nunito+Sans:wght@400;600;700;800;900&family=Open+Sans:ital,wght@0,400;0,600;0,700;1,400&display=swap" rel="stylesheet">
<style>
:root{
  --purple-dark:#5a3891;
  --purple-mid:#6b41a9;
  --purple-soft:#876aae;
  --lavender:#c7ace9;
  --grey-dark:#4b4649;
  --grey-contact:#3e3b3d;
  --grey-light:#eeeeef;
  --ink:#333333;
  --white:#ffffff;
  --accent:#7d52b8;
}
*{margin:0;padding:0;box-sizing:border-box}
html,body{width:1200px;height:3371px;overflow:hidden}
body{position:relative;font-family:"Open Sans",sans-serif;color:var(--ink);background:var(--white)}
section,header,footer{position:absolute;left:0;width:1200px;overflow:hidden}
.abs{position:absolute}
h2.section-title{position:absolute;left:0;width:1200px;text-align:center;font-family:"Nunito Sans",sans-serif;font-weight:800;font-size:36px;letter-spacing:.5px}

/* header */
.site-header{top:0;height:133px;background:var(--purple-dark)}
.brand{left:112px;top:31px;height:72px;display:flex;align-items:center;gap:12px;color:var(--white);font-family:"Nunito Sans",sans-serif;font-weight:800;font-size:26px}
.brand-mark{width:20px;height:20px;background:var(--white)}
.main-nav{display:flex}
.main-nav a{position:absolute;top:58px;color:var(--white);text-decoration:none;font-family:"Nunito Sans",sans-serif;font-weight:700;font-size:14.5px;letter-spacing:.3px}
.main-nav a.active::after{content:"";position:absolute;left:0;right:0;bottom:-8px;height:2px;background:var(--white)}

/* hero */
.hero{top:133px;height:611px;background:linear-gradient(120deg,#7e67b4 0%,#a08ccc 45%,#b7a6d9 70%,#9a83c7 100%)}
.hero-image{position:absolute;inset:0}
.hero-title{position:absolute;left:0;top:193px;width:1200px;text-align:center;color:var(--white);font-family:"Nunito Sans",sans-serif;font-weight:800;font-size:34px;line-height:41px;letter-spacing:.5px}
.hero-arrow{position:absolute;top:200px}

/* about */
.about{top:744px;height:393px;background:var(--lavender)}
.about h2{top:62px;color:#2d2636}
.about-list{position:absolute;left:335px;top:132px;list-style:none}
.about-list li{display:flex;align-items:center;gap:10px;height:52px;font-family:"Nunito Sans",sans-serif;font-weight:700;font-size:18.5px;color:#3a3340}

/* services intro */
.services-intro{top:1137px;height:292px;background:var(--purple-mid);color:var(--white)}
.services-intro h2{top:44px}
.services-intro p{position:absolute;left:180px;width:840px;text-align:center;font-size:13.5px;line-height:23px}

/* services split */
.services-split{top:1429px;height:625px;background:var(--grey-dark)}
.service-col{position:absolute;top:0;color:var(--white)}
.service-col h3{font-family:"Nunito Sans",sans-serif;font-weight:800;font-size:18px;text-decoration:underline;text-underline-offset:4px;margin-bottom:22px}
.service-col ul{list-style:none}
.service-col li{position:absolute;left:26px;font-size:12px;line-height:20px}
.service-col li b{font-weight:700}
.service-col li svg{position:absolute;left:-26px;top:2px}

/* team */
.team{top:2054px;height:643px;background:var(--grey-light)}
.team h2{top:70px;color:#2b2b2b}
.member{position:absolute;top:170px;width:460px;text-align:center}
.member-photo{position:absolute;top:0;width:188px;height:188px;border-radius:50%;border:5px solid var(--white);box-shadow:0 2px 8px rgba(0,0,0,.25)}
.member-title{position:absolute;top:222px;left:0;width:460px;display:flex;justify-content:center;align-items:center;gap:8px}
.member-name{font-family:"Nunito Sans",sans-serif;font-weight:800;font-size:13.5px;color:var(--accent);line-height:20px;text-align:right}
.member-slash{font-size:34px;color:var(--purple-dark);font-weight:300}
.member-role{font-style:italic;font-size:13.5px;color:var(--accent)}
.member-bio{position:absolute;top:272px;left:0;width:460px;font-size:14px;line-height:24px;color:#333}
.read-more{position:absolute;top:356px;left:0;width:460px;font-family:"Nunito Sans",sans-serif;font-weight:800;font-size:14px;color:var(--accent)}

/* contact */
.contact{top:2697px;height:516px;background:var(--grey-contact);color:var(--white)}
.contact h2{top:66px}
.contact-line{position:absolute;left:112px;display:flex;align-items:center;gap:14px;font-size:18px;color:#e4e4e4}
.social{position:absolute;top:304px;width:34px;height:34px;border-radius:50%;background:var(--accent)}
.contact-form{position:absolute;left:643px;top:186px;width:445px}
.field{position:absolute;left:0;width:445px;background:var(--white);font-size:12px;color:#888;padding:9px 12px;border:1px solid #d0d0d0}
.send{position:absolute;left:352px;top:202px;width:93px;height:36px;background:var(--accent);color:var(--white);font-family:"Nunito Sans",sans-serif;font-weight:700;font-size:13px;display:flex;align-items:center;justify-content:center}

/* footer */
.site-footer{top:3213px;height:158px;background:var(--purple-dark);color:var(--white);overflow:visible}
.to-top{position:absolute;left:555px;top:-44px;width:90px;height:90px;border-radius:50%;background:var(--purple-dark)}
.to-top-label{position:absolute;left:0;top:33px;width:1200px;text-align:center;font-family:"Nunito Sans",sans-serif;font-weight:700;font-size:12px;letter-spacing:.5px}
.copyright{position:absolute;left:0;top:88px;width:1200px;text-align:center;font-size:12.5px}
</style>
</head>
<body>

<header class="site-header">
  <div class="brand abs"><span class="brand-mark"></span>ClearPath Health Solutions</div>
  <nav class="main-nav">
    <a href="#" class="active" style="left:484px">HOME</a>
    <a href="#" style="left:578px">ABOUT US</a>
    <a href="#" style="left:697px">OUR SERVICES</a>
    <a href="#" style="left:844px">TEAM</a>
    <a href="#" style="left:935px">CONTACT US</a>
  </nav>
</header>

<section class="hero">
  <div class="hero-image" role="img" aria-label="Photo of a business handshake over a desk with a laptop and clipboard, tinted purple"></div>
  <svg class="hero-arrow" style="left:34px" width="20" height="36" viewBox="0 0 20 36"><path d="M17 2 3 18l14 16" fill="none" stroke="rgba(255,255,255,.7)" stroke-width="3"/></svg>
  <svg class="hero-arrow" style="left:1146px" width="20" height="36" viewBox="0 0 20 36"><path d="M3 2l14 16L3 34" fill="none" stroke="rgba(255,255,255,.7)" stroke-width="3"/></svg>
  <h1 class="hero-title">INCREASING THE VALUE AND SECURITY<br>OF YOUR TECHNOLOGY RESOURCES</h1>
</section>

<section class="about">
  <h2 class="section-title">ABOUT US</h2>
  <ul class="about-list">
    <li><svg width="20" height="20" viewBox="0 0 20 20"><circle cx="10" cy="10" r="10" fill="var(--purple-soft)"/><path d="M5.5 10.5l3 3 6-6.5" fill="none" stroke="#fff" stroke-width="2.2"/></svg>Understand and get to know customer and their needs</li>
    <li><svg width="20" height="20" viewBox="0 0 20 20"><circle cx="10" cy="10" r="10" fill="var(--purple-soft)"/><path d="M5.5 10.5l3 3 6-6.5" fill="none" stroke="#fff" stroke-width="2.2"/></svg>Committed to be a partner, not vendor</li>
    <li><svg width="20" height="20" viewBox="0 0 20 20"><circle cx="10" cy="10" r="10" fill="var(--purple-soft)"/><path d="M5.5 10.5l3 3 6-6.5" fill="none" stroke="#fff" stroke-width="2.2"/></svg>Provide simplified change management expertise</li>
  </ul>
</section>

<section class="services-intro">
  <h2 class="section-title">OUR SERVICES</h2>
  <p style="top:111px">We understand different organizations have different needs. ClearPath HCS strives to assist your organization by bringing solutions that are easy to understand and allow the customer to track success. We provide solutions based on the customer's needs and desires.</p>
  <p style="top:180px">Typically, all services provided by ClearPath HCS will also include a defined deliverable. The purpose is the ensure the value we provide to our customers can be clearly identified and defined prior to the work getting started.</p>
</section>

<section class="services-split">
  <svg class="abs" style="left:0;top:0" width="1200" height="625" viewBox="0 0 1200 625">
    <polygon points="0,0 546,0 611,625 0,625" fill="var(--purple-soft)"/>
    <line x1="546" y1="0" x2="611" y2="625" stroke="#fff" stroke-width="7"/>
  </svg>
  <div class="service-col" style="left:112px;top:70px;width:420px">
    <h3>Electronic Health Record (EHR) Services</h3>
    <ul>
      <li style="top:54px;width:400px"><svg width="16" height="14" viewBox="0 0 16 14"><path d="M1 7h13M8 1l6 6-6 6" fill="none" stroke="#fff" stroke-width="2.4"/></svg><b>EHR Optimization Services</b> - Provide guidance and resources to assist with improving the effective use of the customer's EHR system.</li>
      <li style="top:124px;width:400px"><svg width="16" height="14" viewBox="0 0 16 14"><path d="M1 7h13M8 1l6 6-6 6" fill="none" stroke="#fff" stroke-width="2.4"/></svg><b>EHR Implementation</b> - Assist or conduct a complete EHR implementation.</li>
      <li style="top:194px;width:400px"><svg width="16" height="14" viewBox="0 0 16 14"><path d="M1 7h13M8 1l6 6-6 6" fill="none" stroke="#fff" stroke-width="2.4"/></svg><b>EHR Assessment</b> - Provide a high-level assessment of an organization and how they are currently utilizing this system</li>
      <li style="top:264px;width:400px"><svg width="16" height="14" viewBox="0 0 16 14"><path d="M1 7h13M8 1l6 6-6 6" fill="none" stroke="#fff" stroke-width="2.4"/></svg><b>EHR Quality Assessment</b> - Provide a customized quality assessment to assist with improving quality indicator scores.</li>
      <li style="top:334px;width:400px"><svg width="16" height="14" viewBox="0 0 16 14"><path d="M1 7h13M8 1l6 6-6 6" fill="none" stroke="#fff" stroke-width="2.4"/></svg><b>On-Going EHR Support</b> - Provide on-going support for an organization on a monthly fee basis</li>
    </ul>
  </div>
  <div class="service-col" style="left:670px;top:70px;width:420px">
    <h3>Information Technology Services</h3>
    <ul>
      <li style="top:54px;width:400px"><svg width="16" height="14" viewBox="0 0 16 14"><path d="M1 7h13M8 1l6 6-6 6" fill="none" stroke="#fff" stroke-width="2.4"/></svg><b>Risk Assessment</b> - Provide comprehensive risk assessment including identifying all risks associated with the customer's electronic protected health information (ePHI).</li>
      <li style="top:134px;width:400px"><svg width="16" height="14" viewBox="0 0 16 14"><path d="M1 7h13M8 1l6 6-6 6" fill="none" stroke="#fff" stroke-width="2.4"/></svg><b>Policy Management and Consulting</b> - Provide guidance on IT policy management, particularly policies required and recommended by national Health Insurance Portability and Accountability Act (HIPAA) guidelines.</li>
      <li style="top:228px;width:400px"><svg width="16" height="14" viewBox="0 0 16 14"><path d="M1 7h13M8 1l6 6-6 6" fill="none" stroke="#fff" stroke-width="2.4"/></svg><b>Chief Information Officer (CIO) Services</b> - Act as the organization's CIO or IT Director to assist with improving department's functions and effectiveness.</li>
      <li style="top:298px;width:400px"><svg width="16" height="14" viewBox="0 0 16 14"><path d="M1 7h13M8 1l6 6-6 6" fill="none" stroke="#fff" stroke-width="2.4"/></svg><b>Chief Information Security Officer (CISO) Services</b> - Act as the organization's CISO or Information Security Officer to assist with improving department's functions and effectiveness</li>
      <li style="top:374px;width:400px"><svg width="16" height="14" viewBox="0 0 16 14"><path d="M1 7h13M8 1l6 6-6 6" fill="none" stroke="#fff" stroke-width="2.4"/></svg><b>IT Department Evaluation</b> - Evaluate the department to determine potential changes or issues based on customer perceptions of department</li>
      <li style="top:452px;width:400px"><svg width="16" height="14" viewBox="0 0 16 14"><path d="M1 7h13M8 1l6 6-6 6" fill="none" stroke="#fff" stroke-width="2.4"/></svg><b>On-Going CIO or CISO Support</b> - Provide on-going support for an organization on a monthly fee basis</li>
    </ul>
  </div>
</section>

<section class="team">
  <h2 class="section-title">OUR TEAM</h2>
  <div class="member" style="left:87px">
    <div class="member-photo" role="img" aria-label="Portrait photo of the president and CEO at a desk" style="left:136px;background:linear-gradient(160deg,#c9d3dc,#2f3a4c)"></div>
    <div class="member-title"><span class="member-name">Daniel Reyes, MHA, MBA,<br>CHCIO, CPHIMS</span><span class="member-slash">/</span><span class="member-role">President and CEO</span></div>
    <p class="member-bio">As the Founder and CEO of ClearPath HCS. Daniel has been working in the technology industry for over 25 years with extensive experience in healthcare and IT...</p>
    <a class="read-more">Read More »</a>
  </div>
  <div class="member" style="left:643px">
    <div class="member-photo" role="img" aria-label="Portrait photo of the vice president and COO in a white coat" style="left:136px;background:linear-gradient(160deg,#eef0f2,#c9cfd6)"></div>
    <div class="member-title"><span class="member-name">Marta Lindgren, BSW,<br>MA</span><span class="member-slash">/</span><span class="member-role">Vice President and COO</span></div>
    <p class="member-bio">As the VP and Chief Operating Officer at ClearPath HCS, Marta is passionate about providing an excellent customer experience. Marta has extensive experience working...</p>
    <a class="read-more">Read More »</a>
  </div>
</section>

<section class="contact">
  <h2 class="section-title">CONTACT US</h2>
  <div class="contact-line" style="top:200px"><svg width="16" height="16" viewBox="0 0 24 24"><path d="M6.6 10.8a15 15 0 0 0 6.6 6.6l2.2-2.2c.3-.3.7-.4 1-.2 1.1.4 2.3.6 3.6.6.6 0 1 .4 1 1V20c0 .6-.4 1-1 1A17 17 0 0 1 3 4c0-.6.4-1 1-1h3.5c.6 0 1 .4 1 1 0 1.3.2 2.5.6 3.6.1.3 0 .7-.2 1z" fill="var(--accent)"/></svg>Call us at 515-555-0148</div>
  <div class="contact-line" style="top:242px"><svg width="16" height="12" viewBox="0 0 16 12"><rect width="16" height="12" rx="1" fill="var(--accent)"/><path d="M1 1l7 5 7-5" fill="none" stroke="var(--grey-contact)" stroke-width="1.4"/></svg>Email us at dreyes@clearpathhcs.example</div>
  <span class="social" style="left:113px"></span>
  <span class="social" style="left:154px"></span>
  <span class="social" style="left:194px"></span>
  <div class="contact-form">
    <div class="field" style="top:0;height:34px">Name *</div>
    <div class="field" style="top:40px;height:34px">Email *</div>
    <div class="field" style="top:81px;height:34px">Subject</div>
    <div class="field" style="top:121px;height:74px">Message</div>
    <div class="send">SEND</div>
  </div>
</section>

<footer class="site-footer">
  <div class="to-top"><svg class="abs" style="left:36px;top:16px" width="18" height="20" viewBox="0 0 18 20"><path d="M9 19V3M2 10l7-7 7 7" fill="none" stroke="#fff" stroke-width="3"/></svg></div>
  <div class="to-top-label">BACK TO TOP</div>
  <div class="copyright">Copyrights © 2018 CLEARPATH HEALTH SOLUTIONS. All Rights Reserved.</div>
</footer>

</body>
</html>
```